Moravel Swim Stationary

Recently established Aquatics Club, with competitive swimming being a principal activity needs stationary, including business cards, letterhead and envelopes, application forms.
The designs shold incorporate the Club's logo. ( The colours are aqua and teal)
The statonary should be fun yet project a corporate image sufficient to attract potential sponsors.

Club members, sponsors, professional organisations.

Business

• Club Logo
Address & Telephone number

The letterhead must contain the Club's Mission Statement.
It can be incorporated in the "footer" on the page.

To provide aquatics programmes, for persons of all ages, that encourage physical fitness and wellness, build character and self-discipline, inspire camaraderie and promote civic mindedness and excellence.

```html
<!DOCTYPE html>
<html lang="en">
<head>
<meta charset="utf-8">
<title>Moravel Swim – Business Cards</title>
<link rel="stylesheet" href="https://fonts.googleapis.com/css2?family=Lato:wght@400;700&display=swap">
<style>
  :root {
    --stage: #3b3b3d;
    --card-white: #f7f7f5;
    --card-black: #1c1a1b;
    --orange: #ef7d1f;
    --teal: #11897d;
    --ink: #555657;
    --rule: #c9c9c9;
  }
  * { margin: 0; padding: 0; box-sizing: border-box; }
  html, body { width: 1200px; height: 840px; overflow: hidden; }
  body {
    background: var(--stage);
    font-family: "Lato", Arial, sans-serif;
    position: relative;
  }
  .card {
    position: absolute;
    width: 525px;
    height: 300px;
    border-radius: 3px;
    overflow: hidden;
    box-shadow: 0 12px 30px rgba(0,0,0,.45);
  }
  .card-back { left: 150px; top: 70px; background: var(--card-black); }
  .card-front { left: 525px; top: 470px; background: var(--card-white); }

  .wordmark {
    display: flex;
    align-items: center;
    gap: 10px;
    font-weight: 700;
    font-size: 34px;
    color: var(--orange);
    white-space: nowrap;
  }
  .wordmark-dot {
    width: 18px; height: 18px; border-radius: 50%;
    background: var(--teal);
    flex: none;
  }

  .card-back .wordmark {
    position: absolute; left: 50%; top: 110px; transform: translateX(-50%);
  }
  .back-web {
    position: absolute; left: 0; right: 0; top: 200px;
    text-align: center; color: #fff; font-size: 14px; letter-spacing: .3px;
  }

  .card-front .wordmark {
    position: absolute; left: 134px; top: 124px; transform: translateX(-50%);
    font-size: 28px; gap: 8px;
  }
  .card-front .wordmark-dot { width: 15px; height: 15px; }
  .divider {
    position: absolute; left: 268px; top: 42px; width: 1px; height: 170px;
    background: var(--rule);
  }
  .contact { position: absolute; left: 294px; top: 34px; color: var(--ink); }
  .contact-name { color: var(--orange); font-size: 17px; font-weight: 400; }
  .contact-role { font-size: 12px; margin-top: 2px; }
  .contact-address { font-size: 12px; line-height: 1.35; margin-top: 18px; }
  .contact-lines { list-style: none; margin-top: 10px; font-size: 12px; line-height: 1.4; }
  .contact-lines li { display: flex; align-items: center; gap: 8px; }
  .contact-lines svg { width: 10px; height: 10px; fill: var(--teal); flex: none; }
  .edge { position: absolute; left: 0; bottom: 0; width: 525px; height: 300px; }
</style>
</head>
<body>
  <section class="card card-back" aria-label="Business card back">
    <div class="wordmark"><span class="wordmark-dot"></span>Moravel Swim</div>
    <p class="back-web">www.moravelswim.com</p>
  </section>

  <section class="card card-front" aria-label="Business card front">
    <svg class="edge" viewBox="0 0 525 300" aria-hidden="true">
      <path d="M0 278 H430 C455 278 462 262 468 248 C474 236 484 232 525 232 V300 H0 Z" fill="var(--orange)"/>
      <path d="M472 246 C478 236 488 218 525 216 V232 C490 232 480 236 472 246 Z" fill="var(--teal)"/>
      <path d="M482 226 C490 214 500 208 525 206 V216 C500 218 490 222 482 226 Z" fill="var(--teal)"/>
    </svg>

    <div class="wordmark"><span class="wordmark-dot"></span>Moravel Swim</div>
    <div class="divider"></div>

    <div class="contact">
      <h1 class="contact-name">Daniel Okafor</h1>
      <p class="contact-role">Director</p>
      <p class="contact-address">123 Address Line 1<br>Address Line 2<br>City Code</p>
      <ul class="contact-lines">
        <li><svg viewBox="0 0 10 10"><path d="M2 0 L4 2 L3 4 Q4.5 6 6 7 L8 6 L10 8 L8 10 Q3 9 0 2 Z"/></svg>+123.456.7890</li>
        <li><svg viewBox="0 0 10 10"><rect x="2" y="0" width="6" height="3"/><rect x="0" y="3" width="10" height="5" rx="1"/><rect x="2" y="7" width="6" height="3"/></svg>+123.456.7891</li>
        <li><svg viewBox="0 0 10 10"><path d="M2.5 0 H7.5 V10 H2.5 Z M3.5 1 V8 H6.5 V1 Z"/></svg>+123.456.7892</li>
        <li><svg viewBox="0 0 10 10"><path d="M0 2 H10 L5 6 Z M0 3 L5 7 L10 3 V9 H0 Z"/></svg>daniel@moravelswim.com</li>
        <li><svg viewBox="0 0 10 10"><circle cx="5" cy="5" r="5"/><path d="M0 5 H10 M5 0 V10" stroke="#fff" stroke-width=".8"/></svg>www.moravelswim.com</li>
      </ul>
    </div>
  </section>
</body>
</html>
```